Catalog for our Gold Coins for high value market

We need someone who makes our catalog or book for the gold coins of Switzerland.
Please use the Word Document. The text and the images are below. Feel free to make a nice design. Also make a nice design as a title.
Please use Adobe Indesign or Illustrator to make the content adjustable for us if needed.

You could also add a "star rating" from 1-4 for some of the coins with an image. I will do the rating later. It should be a rating of how precious the coins are without entering a price.
You could also adjust the title design with the coins.

Please make at least the following pages:
Title
Table of content
Title Page for each Ares (Aargau Page 6, Appenzell Page 6, Basel Page 8 and so on)
Pages with the content (Coins including the description)

Target Market(s)

Gold coins collectors. Usually those people are rich men.

Requirements
Must have
• Modern design
Should not have
• Not too many colors used. It should be modern. But have some class.

```html
<!DOCTYPE html>
<html lang="de">
<head>
<meta charset="utf-8">
<title>Goldmünzen der Kantone und Eidgenossenschaft – Catalog</title>
<link rel="stylesheet" href="https://fonts.googleapis.com/css2?family=Open+Sans:wght@700;800&family=Source+Sans+3:wght@400;600;700&display=swap">
<style>
  :root{
    --board:#a3a8aa;
    --shadow:#7d8386;
    --paper:#ffffff;
    --gold-pale:#fdd088;
    --gold:#fbb040;
    --orange:#f39432;
    --accent:#e8412c;
    --rule-blue:#2b4fa0;
    --ink:#231f20;
    --coin-hi:#f6d978;
    --coin-mid:#d9a63a;
    --coin-lo:#9c6a1c;
  }
  *{box-sizing:border-box;margin:0;padding:0}
  html,body{width:1200px;height:1200px;overflow:hidden}
  body{background:var(--board);font-family:"Source Sans 3",Arial,sans-serif;color:var(--ink);position:relative}

  .shadow{position:absolute;background:var(--shadow)}
  .page{position:absolute;background:var(--paper);overflow:hidden}
  .abs{position:absolute}

  /* Cover */
  .cover{left:27px;top:189px;width:497px;height:696px;background:var(--gold-pale)}
  .cover-top{left:0;top:0;width:100%;height:108px;background:var(--gold)}
  .cover-title-box{left:30px;top:30px;width:423px;height:128px;background:var(--orange)}
  .cover-frame{left:57px;top:70px;width:369px;height:76px;border:1.5px solid var(--paper)}
  .cover-title{left:81px;top:77px;color:var(--paper);font-size:21px;line-height:25px;font-weight:400}
  .cover-tag{left:282px;top:132px;width:139px;height:27px;background:var(--paper);color:#000;font-size:21px;line-height:27px;text-align:center}
  .cover-medal{left:136px;top:208px;width:226px;height:226px;border-radius:50%;border:3px solid var(--paper);background:var(--orange);display:flex;align-items:center;justify-content:center}
  .cover-medal .coin{width:206px;height:206px}
  .cover-strip{left:0;top:440px;width:100%;height:120px;background:var(--paper)}
  .cover-strip .coin{position:absolute;width:90px;height:90px;top:14px}

  .coin{border-radius:50%;background:radial-gradient(circle at 38% 35%,var(--coin-hi),var(--coin-mid) 55%,var(--coin-lo));}

  /* Contents page */
  .toc-logo{left:214px;top:16px;font-weight:700;font-size:10px;color:var(--accent);display:flex;align-items:center;gap:4px}
  .toc-logo .mark{width:7px;height:7px;background:var(--accent)}
  .toc-heading{left:21px;top:31px;font-family:"Open Sans",sans-serif;font-weight:800;font-size:11px;letter-spacing:1.5px}
  .toc-list{left:5px;top:47px;width:290px;list-style:none}
  .toc-list li{display:flex;align-items:center;height:7.45px;font-size:5.4px;line-height:7.45px}
  .toc-list .label{padding-left:16px;white-space:nowrap}
  .toc-list .fill{flex:1;border-bottom:0.8px dashed var(--gold);margin:0 6px 0 5px;height:0}
  .toc-list .num{width:10px;text-align:right}
  .toc-list .section .label{background:var(--gold);color:var(--paper);width:74px;padding-left:16px}
  .toc-list .gap{margin-top:3px}

  /* Chapter pages */
  .band{left:0;width:100%;height:19px;background:var(--gold);color:var(--paper);font-family:"Open Sans",sans-serif;font-weight:700;font-size:10.5px;line-height:19px;padding-left:17px}
  .subhead{font-family:"Open Sans",sans-serif;font-weight:700;font-size:6.6px;letter-spacing:.4px;color:var(--accent);border-bottom:0.8px solid var(--gold);padding-bottom:1px}
  .body-text{font-size:5.3px;line-height:7.3px;text-align:justify;width:284px}
  .stars{font-size:11px;color:var(--gold);letter-spacing:1px;line-height:1;text-align:center;width:70px}
  .caption{font-size:5.3px;line-height:7.3px;padding:3px 6px;border-left:0.8px solid var(--gold);border-right:0.8px solid var(--gold);text-align:left}
  .caption::before,.caption::after{content:"";position:absolute;top:0;bottom:0;width:4px;border-top:0.8px solid var(--gold);border-bottom:0.8px solid var(--gold)}
  .caption::before{left:0}
  .caption::after{right:0}
  .caption.center{text-align:center}
  .divider{height:0;border-top:0.8px solid var(--gold)}
  .page-num{font-size:5.5px;width:100%;text-align:center;left:0}
  .bullets{font-size:5.4px;line-height:7.4px;list-style:none}
  .bullets li::before{content:"●";font-size:4px;margin-right:5px;vertical-align:1px}
  .note{font-size:3.8px}

  .caption-line{left:0;top:1155px;width:100%;text-align:center;font-size:20px;color:var(--ink);letter-spacing:-.2px}
  .caption-line strong{font-weight:700}
</style>
</head>
<body>

<!-- Cover -->
<div class="shadow" style="left:19px;top:199px;width:484px;height:696px"></div>
<section class="page cover">
  <div class="abs cover-top"></div>
  <div class="abs cover-title-box"></div>
  <div class="abs cover-frame"></div>
  <h1 class="abs cover-title">Goldmünzen<br>der Kantone und Eidgenossenschaft</h1>
  <div class="abs cover-tag">Catalog</div>
  <div class="abs cover-medal">
    <div class="coin" role="img" aria-label="Goldmünze mit Wappentier und Umschrift IN PACE DOMINE CONSERVA NOS"></div>
  </div>
  <div class="abs cover-strip">
    <div class="coin" style="left:65px" role="img" aria-label="Goldmünze Respublica Bernensis mit Wappen"></div>
    <div class="coin" style="left:157px" role="img" aria-label="Goldmünze 100 Franken 1925"></div>
    <div class="coin" style="left:248px" role="img" aria-label="Goldmünze 20 Franken mit Schweizerkreuz"></div>
    <div class="coin" style="left:340px" role="img" aria-label="Goldmünze Canton Solothurn 1813"></div>
  </div>
</section>

<!-- Contents -->
<div class="shadow" style="left:533px;top:161px;width:300px;height:443px"></div>
<section class="page" style="left:539px;top:152px;width:316px;height:443px">
  <div class="abs toc-logo"><span class="mark"></span>AURUM VOGEL</div>
  <h2 class="abs toc-heading">INHALT</h2>
  <ul class="abs toc-list">
    <li class="section"><span class="label">Aargau</span><span class="fill"></span><span class="num">6</span></li>
    <li><span class="label">Abt Anselm von Hohenrain 1684 – 1723</span><span class="fill"></span><span class="num">6</span></li>
    <li class="section"><span class="label">Appenzell</span><span class="fill"></span><span class="num">6</span></li>
    <li><span class="label">Appenzell Innerrhoden</span><span class="fill"></span><span class="num">6</span></li>
    <li class="section"><span class="label">Basel</span><span class="fill"></span><span class="num">6</span></li>
    <li><span class="label">Reichsmünzstätte</span><span class="fill"></span><span class="num">7</span></li>
    <li><span class="label">Reichsmünzstätte 15. Jahrhundert</span><span class="fill"></span><span class="num">7</span></li>
    <li><span class="label">Stadt Basel 16. Jahrhundert</span><span class="fill"></span><span class="num">8</span></li>
    <li><span class="label">Stadt Basel 17. Jahrhundert</span><span class="fill"></span><span class="num">13</span></li>
    <li><span class="label">Stadt Basel 18. Jahrhundert</span><span class="fill"></span><span class="num">14</span></li>
    <li><span class="label">Bistum Basel</span><span class="fill"></span><span class="num">16</span></li>
    <li><span class="label">Johann Franz von Eichwald 1651 -1656</span><span class="fill"></span><span class="num">19</span></li>
    <li><span class="label">Johann Konrad I. von Tannberg 1656-1693</span><span class="fill"></span><span class="num">19</span></li>
    <li><span class="label">Johann Konrad II. von Rheinfeld-Hirschau 1705-1737</span><span class="fill"></span><span class="num">19</span></li>
    <li class="section gap"><span class="label">Bern</span><span class="fill"></span><span class="num">20</span></li>
    <li><span class="label">Bern – 15. Jahrhundert</span><span class="fill"></span><span class="num">20</span></li>
    <li><span class="label">Bern – 16. Jahrhundert</span><span class="fill"></span><span class="num">20</span></li>
    <li><span class="label">Bern – 17. Jahrhundert</span><span class="fill"></span><span class="num">20</span></li>
    <li><span class="label">Bern – 18. Jahrhundert</span><span class="fill"></span><span class="num">20</span></li>
    <li><span class="label">Bern – 19. Jahrhundert</span><span class="fill"></span><span class="num">20</span></li>
    <li class="section gap"><span class="label">Freiburg / Fribourg</span><span class="fill"></span><span class="num">48</span></li>
    <li><span class="label">Freiburg / Fribourg – 15. / 16. Jahrhundert</span><span class="fill"></span><span class="num">49</span></li>
    <li><span class="label">Freiburg / Fribourg – 16. Jahrhundert</span><span class="fill"></span><span class="num">49</span></li>
    <li><span class="label">Freiburg / Fribourg – 17. Jahrhundert</span><span class="fill"></span><span class="num">50</span></li>
    <li class="section"><span class="label">Genf / Genève</span><span class="fill"></span><span class="num">51</span></li>
    <li><span class="label">Genf / Genève – 16. Jahrhundert</span><span class="fill"></span><span class="num">52</span></li>
    <li><span class="label">Genf / Genève – 17. Jahrhundert</span><span class="fill"></span><span class="num">53</span></li>
    <li><span class="label">Genf / Genève – 18. Jahrhundert</span><span class="fill"></span><span class="num">54</span></li>
    <li><span class="label">Genf / Genève – Dezimalsystem von 1838 – 1848</span><span class="fill"></span><span class="num">54</span></li>
    <li class="section"><span class="label">Graubünden</span><span class="fill"></span><span class="num">55</span></li>
    <li><span class="label">Bistum Chur</span><span class="fill"></span><span class="num">55</span></li>
    <li><span class="label">Peter II. Ranser 1581 – 1601</span><span class="fill"></span><span class="num">56</span></li>
    <li><span class="label">Johann V. Falk von Adlerberg 1601 – 1627</span><span class="fill"></span><span class="num">56</span></li>
    <li><span class="label">Johann VI. Falk von Adlerberg 1636 – 1661</span><span class="fill"></span><span class="num">57</span></li>
    <li><span class="label">Ulrich VI. von Bergau 1661 – 1692</span><span class="fill"></span><span class="num">58</span></li>
    <li><span class="label">Ulrich VII. von Federhain 1692 - 1728</span><span class="fill"></span><span class="num">58</span></li>
    <li><span class="label">Joseph Benedikt von Rosenau 1728 – 1754</span><span class="fill"></span><span class="num">59</span></li>
    <li><span class="label">Johann Anton von Federhain 1755 – 1777</span><span class="fill"></span><span class="num">60</span></li>
    <li><span class="label">Stadt Chur</span><span class="fill"></span><span class="num">61</span></li>
    <li><span class="label">Stadt Chur – 17. Jahrhundert</span><span class="fill"></span><span class="num">61</span></li>
    <li><span class="label">Stadt Chur – 18. Jahrhundert</span><span class="fill"></span><span class="num">62</span></li>
    <li><span class="label">Graubünden – Herrschaft Haldenstein</span><span class="fill"></span><span class="num">63</span></li>
    <li><span class="label">Thomas I. von Schattenburg 1609 - 1628</span><span class="fill"></span><span class="num">63</span></li>
    <li><span class="label">Julius Otto I. von Schattenburg 1628 – 1666</span><span class="fill"></span><span class="num">63</span></li>
    <li><span class="label">Thomas II. von Schattenburg 1666 – 1667</span><span class="fill"></span><span class="num">64</span></li>
    <li><span class="label">Georg Philipp von Schattenburg 1671 – 1695</span><span class="fill"></span><span class="num">65</span></li>
    <li><span class="label">Thomas von Saland 1737 – 1783</span><span class="fill"></span><span class="num">66</span></li>
    <li><span class="label">Graubünden - Misox</span><span class="fill"></span><span class="num">67</span></li>
  </ul>
</section>

<!-- Page 6 -->
<div class="shadow" style="left:858px;top:161px;width:306px;height:443px"></div>
<section class="page" style="left:864px;top:152px;width:316px;height:443px">
  <div class="abs band" style="top:0;height:22px;line-height:26px">AARGAU</div>
  <div class="abs subhead" style="left:17px;top:24px;width:170px">Abt Anselm von Hohenrain 1684 – 1723</div>
  <p class="abs body-text" style="left:17px;top:37px">Anselm Hohenrain (* 13. August 1646 in Bremgarten; † 14. September 1723 auf Schloss Sandegg) war ein Schweizer Benediktinermönch. Von 1684 bis 1701 war er Abt, danach bis zu seinem Tod erster Fürstabt des Klosters Muri in den Freien Ämtern (im heutigen Kanton Aargau).</p>
  <div class="abs divider" style="left:17px;top:59px;width:237px;border-color:var(--rule-blue)"></div>

  <div class="abs coin" style="left:17px;top:70px;width:57px;height:57px" role="img" aria-label="5 Dukaten 1720, Vorderseite mit Klosteransicht"></div>
  <div class="abs coin" style="left:89px;top:70px;width:57px;height:57px" role="img" aria-label="5 Dukaten 1720, Rückseite mit Bildnis des Abtes"></div>
  <div class="abs coin" style="left:164px;top:70px;width:57px;height:57px" role="img" aria-label="Dukat 1720, Vorderseite mit Bildnis des Abtes"></div>
  <div class="abs coin" style="left:236px;top:70px;width:57px;height:57px" role="img" aria-label="Dukat 1720, Rückseite mit Wappen"></div>
  <div class="abs stars" style="left:42px;top:136px">★★★☆</div>
  <div class="abs stars" style="left:190px;top:132px">★★★☆</div>
  <div class="abs caption center" style="left:26px;top:151px;width:102px">5 Dukaten (Jahr 1720, HMZ 2-11a)</div>
  <div class="abs caption center" style="left:178px;top:146px;width:95px">Dukat (Jahr 1720, HMZ 2-12a)</div>

  <div class="abs band" style="top:181px">Appenzell</div>
  <div class="abs subhead" style="left:17px;top:204px;width:100px">Appenzell Innerrhoden</div>
  <div class="abs coin" style="left:17px;top:227px;width:57px;height:57px" role="img" aria-label="Dukat 1737, Vorderseite mit stehendem Bären"></div>
  <div class="abs coin" style="left:89px;top:227px;width:57px;height:57px" role="img" aria-label="Dukat 1737, Rückseite mit Schrift"></div>
  <div class="abs coin" style="left:164px;top:227px;width:57px;height:57px" role="img" aria-label="Dukat 1739, Vorderseite mit stehendem Bären"></div>
  <div class="abs coin" style="left:236px;top:227px;width:57px;height:57px" role="img" aria-label="Dukat 1739, Rückseite mit Schrifttafel"></div>
  <div class="abs stars" style="left:42px;top:288px">★★★☆</div>
  <div class="abs stars" style="left:190px;top:288px">★★★☆</div>
  <div class="abs caption center" style="left:34px;top:301px;width:86px">Dukat (Jahr 1737, HMZ 2-35a)</div>
  <div class="abs caption center" style="left:184px;top:300px;width:84px">Dukat (Jahr 1739, HMZ 2-35b)</div>

  <div class="abs band" style="top:327px">Basel</div>
  <p class="abs body-text" style="left:17px;top:350px">Münzen mit der Aufschrift BASILIA sind uns bereits seit der 2. Hälfte des 7. Jahrhunderts bekannt. Auch in der Karolingerzeit und unter der burgundischen Herrschaft wurden in Basel Münzen geprägt. Das Münzrecht ging dann in der Regierungszeit von Bischof Ortwin (999 bis 1025) an das Bistum über. Bischof Berthold III. (1366-1382) verpfändete das Münzrecht der Stadt Basel 1373, was praktisch einem Verkauf gleichkam, da das Bistum nie mehr in der Lage war, dieses zurückzukaufen. Im Vertrag von 1585 mit Bischof Jakob Christoph Wendel wurde der Verkauf noch endgültig getätigt. Das Bistum verlor aber die eigene Münzberechtigung nicht, und Wendel münzte selber 1586 bzw. ab 1595 in Delsberg und St. Ursanne weiter. Sein Nachfolger richtete 1623 in Pruntrut eine Münzstätte ein, die mit zwei längeren Unterbrüchen bis 1787 in Betrieb war. Der deutsche König Gerold errichtete 1429 in Basel eine Reichsgold-Münzstätte, welche bis 1509 in Betrieb war.</p>
  <div class="abs page-num" style="top:426px">6</div>
</section>

<!-- Page 7 -->
<div class="shadow" style="left:533px;top:621px;width:300px;height:443px"></div>
<section class="page" style="left:539px;top:612px;width:316px;height:443px">
  <p class="abs body-text" style="left:16px;top:13px">Gerechnet wurde in Basel nach:</p>
  <ul class="abs bullets" style="left:16px;top:21px">
    <li>Basler Pfund zu 20 Schilling (Sols) zu 12 Deniers</li>
    <li>Basler Gulden zu 25 Schilling zu 12 Deniers</li>
    <li>Basler Gulden zu 15 Batzen zu 4 Kreuzer und 8 Heller</li>
    <li>Schweizer Franken zu 10 Batzen zu 10 Rappen</li>
  </ul>
  <p class="abs note" style="left:16px;top:52px">Schutzpatronin: Jungfrau Maria (bis zur Reformation)</p>
  <div class="abs subhead" style="left:16px;top:63px;width:82px">Reichsmünzstätte</div>
  <p class="abs body-text" style="left:16px;top:74px">Auf Empfehlung seines Reichskämmerers, Konrad von Lindenau, entschloss sich König Gerold in Basel eine Prägestätte für Goldgulden zu eröffnen, vor allem auch, da ein päpstliches Konzil in Basel vorgesehen war. Die Ende 1429 eröffnete Reichsmünzstätte war von derjenigen der Stadt Basel vollkommen abgetrennt, und es wurden in den folgenden 80 Jahren eine grosse Anzahl Goldgulden geschlagen. 1509 siedelte diese Münzstätte nach Augsburg über, und die Stadt Basel musste um ihre Bedeutung als Handelsplatz fürchten. In der Folge bemühte sich der städtische Rat darum, schnellstmöglich ein eigenes Recht zur Goldprägung zu erhalten, was ihm der Papst 1512 erteilte. 1516 bestätigte der Kaiser dieses Recht ebenfalls, nachdem unter seiner Verantwortung im selben Jahr die letzten Reichsgoldgulden in Basel geschlagen wurden.</p>
  <div class="abs subhead" style="left:16px;top:141px;width:150px">Reichsmünzstätte 15. Jahrhundert</div>

  <div class="abs coin" style="left:31px;top:159px;width:58px;height:58px" role="img" aria-label="Goldgulden König, Vorderseite"></div>
  <div class="abs coin" style="left:95px;top:159px;width:58px;height:58px" role="img" aria-label="Goldgulden König, Rückseite"></div>
  <div class="abs coin" style="left:163px;top:159px;width:58px;height:58px" role="img" aria-label="Goldgulden Kaiser, Vorderseite"></div>
  <div class="abs coin" style="left:227px;top:159px;width:58px;height:58px" role="img" aria-label="Goldgulden Kaiser, Rückseite"></div>
  <div class="abs stars" style="left:53px;top:221px">★★★☆</div>
  <div class="abs stars" style="left:189px;top:219px">★★★☆</div>
  <div class="abs caption" style="left:43px;top:235px;width:87px">Gerold König, Goldgulden (Jahr 1429- 1433, HMZ 2-49 a) mit der Inschrift GEROL … REX</div>
  <div class="abs caption" style="left:177px;top:232px;width:89px">Gerold Kaiser, Goldgulden (Jahr 1433-1437, HMZ 2-49 b) mit der Inschrift GEROL … IMP</div>
  <div class="abs divider" style="left:49px;top:288px;width:237px"></div>

  <div class="abs coin" style="left:31px;top:296px;width:58px;height:58px" role="img" aria-label="Goldgulden Interregnum, Vorderseite"></div>
  <div class="abs coin" style="left:95px;top:296px;width:58px;height:58px" role="img" aria-label="Goldgulden Interregnum, Rückseite"></div>
  <div class="abs coin" style="left:163px;top:296px;width:58px;height:58px" role="img" aria-label="Goldgulden Arnold II., Vorderseite"></div>
  <div class="abs coin" style="left:227px;top:296px;width:58px;height:58px" role="img" aria-label="Goldgulden Arnold II., Rückseite"></div>
  <div class="abs stars" style="left:50px;top:358px">★★★☆</div>
  <div class="abs stars" style="left:192px;top:358px">★★★☆</div>
  <div class="abs caption" style="left:44px;top:373px;width:80px">Interregnum Goldgulden o. J. Ohne Herrschernamen (Jahr 1438 HMZ 2-49 c)</div>
  <div class="abs caption" style="left:181px;top:373px;width:88px">Goldgulden o. J. Arnold II. König (Jahr 1438-1439, HMZ 2-49 d) Rückseite Stadtname</div>
  <div class="abs page-num" style="top:426px">7</div>
</section>

<!-- Page 8 -->
<div class="shadow" style="left:858px;top:621px;width:306px;height:443px"></div>
<section class="page" style="left:864px;top:612px;width:316px;height:443px">
  <div class="abs coin" style="left:30px;top:24px;width:58px;height:58px" role="img" aria-label="Goldgulden Arnold als König, Vorderseite"></div>
  <div class="abs coin" style="left:94px;top:24px;width:58px;height:58px" role="img" aria-label="Goldgulden Arnold als König, Rückseite AVE MARIA"></div>
  <div class="abs coin" style="left:164px;top:24px;width:58px;height:58px" role="img" aria-label="Goldgulden Arnold als König, Vorderseite"></div>
  <div class="abs coin" style="left:229px;top:24px;width:58px;height:58px" role="img" aria-label="Goldgulden Arnold als König, Rückseite SANCTA MARIA"></div>
  <div class="abs stars" style="left:54px;top:95px">★★★☆</div>
  <div class="abs stars" style="left:190px;top:95px">★★★☆</div>
  <div class="abs caption" style="left:49px;top:110px;width:80px">Goldgulden o. J. Arnold als König (Jahr XXXX HMZ 4-49 e) Rückseite AVE MARIA</div>
  <div class="abs caption" style="left:184px;top:110px;width:82px">Goldgulden o. J. Arnold als König (Jahr XXXX HMZ 4-49 f) Rückseite SANCTA MARIA</div>
  <div class="abs divider" style="left:31px;top:148px;width:254px"></div>

  <div class="abs coin" style="left:30px;top:160px;width:58px;height:58px" role="img" aria-label="Goldgulden Gerwin III. König, Vorderseite"></div>
  <div class="abs coin" style="left:94px;top:160px;width:58px;height:58px" role="img" aria-label="Goldgulden Gerwin III. König, Rückseite"></div>
  <div class="abs coin" style="left:164px;top:160px;width:58px;height:58px" role="img" aria-label="Goldgulden Gerwin III. Imperator, Vorderseite"></div>
  <div class="abs coin" style="left:229px;top:160px;width:58px;height:58px" role="img" aria-label="Goldgulden Gerwin III. Imperator, Rückseite"></div>
  <div class="abs stars" style="left:54px;top:223px">★★★☆</div>
  <div class="abs stars" style="left:190px;top:223px">★★★☆</div>
  <div class="abs caption" style="left:49px;top:238px;width:80px">Goldgulden o. J. Gerwin III. König (Jahr 1440-1452 HMZ 2-49 g) GERWI … REX</div>
  <div class="abs caption" style="left:184px;top:238px;width:82px">Goldgulden o. J. Gerwin III. Imperator (Jahr 1452-1478 HMZ 2-49h). GERWI … IMP</div>
  <div class="abs divider" style="left:31px;top:288px;width:254px"></div>

  <div class="abs coin" style="left:97px;top:296px;width:58px;height:58px" role="img" aria-label="Goldgulden 1478-90, Vorderseite"></div>
  <div class="abs coin" style="left:161px;top:296px;width:58px;height:58px" role="img" aria-label="Goldgulden 1478-90, Rückseite"></div>
  <div class="abs stars" style="left:122px;top:358px">★★★☆</div>
  <div class="abs caption" style="left:112px;top:372px;width:83px">Goldgulden o. J. (1478-90 HMZ 2-49 i). Umschrift GERWI…IMP, Rückseite mit</div>
  <div class="abs page-num" style="top:426px">8</div>
</section>

<p class="abs caption-line">A4 SIZE 8.27 X 11.69” WITH BLEED 0.25” | WELL ORGANIZED LAYERS | <strong>PRINT READY FILE</strong></p>

</body>
</html>
```